Campaign Website

I need a website for my judicial campaign. I would like a site that directs from this domain as well as a new domain with my married last name. I need separate pages on the site that address my diversion programs, and a page to allow people to donate with a link to my bank account and a link for people to submit requests to volunteer, get yard signs, etc.

```html
<!DOCTYPE html>
<html lang="en">
<head>
<meta charset="utf-8">
<title>Dana Whitfield for Judge</title>
<link href="https://fonts.googleapis.com/css2?family=Playfair+Display:ital,wght@0,700;1,700&family=Montserrat:wght@400;600;700&display=swap" rel="stylesheet">
<style>
:root{
  --navy:#0f2d6b;
  --navy-bar:#081a42;
  --red:#e5173f;
  --red-soft:#f23a57;
  --white:#ffffff;
  --ink:#1d2333;
  --muted:#6b7080;
  --line:#d9dce4;
  --pale:#d5dcec;
}
*{box-sizing:border-box;margin:0;padding:0}
html,body{width:748px;height:1200px;overflow:hidden}
body{position:relative;font-family:"Montserrat",sans-serif;color:var(--ink);background:var(--white)}
.serif{font-family:"Playfair Display",serif}

/* hero */
.hero{position:absolute;left:0;top:0;width:748px;height:350px;background:var(--navy);overflow:hidden}
.hero-shape{position:absolute;left:0;top:0}
.candidate-photo{position:absolute;left:470px;top:45px;width:220px;height:305px;border-radius:110px 110px 0 0;background:linear-gradient(180deg,#5a3b30 0%,#2a1b18 45%,#141414 100%)}
.nav{position:absolute;top:18px;left:372px;display:flex;align-items:center;gap:14px}
.nav a{color:var(--white);font-size:8px;font-weight:600;letter-spacing:.5px;text-decoration:none}
.nav .nav-cta{margin-left:10px;background:var(--white);color:var(--red);padding:5px 10px;border-radius:10px;font-weight:700}
.hero-title{position:absolute;left:165px;top:112px;width:290px;color:var(--white);font-size:40px;font-weight:700;line-height:1.12}
.hero-actions{position:absolute;left:167px;top:252px;display:flex;gap:12px}
.btn{display:inline-block;font-size:8px;font-weight:700;letter-spacing:.5px;padding:6px 12px;border-radius:12px;text-decoration:none}
.btn-red{background:var(--red);color:var(--white)}
.btn-white{background:var(--white);color:var(--navy)}

/* action cards */
.actions{position:absolute;top:378px;left:144px;display:flex;gap:12px}
.card{width:146px;height:150px;border:1px solid var(--line);border-radius:4px;text-align:center;padding:16px 12px;background:var(--white);box-shadow:0 2px 6px rgba(0,0,0,.08)}
.card-icon{width:26px;height:26px;margin:0 auto 8px;display:block}
.card h3{font-size:13px;font-weight:700;margin-bottom:6px}
.card p{font-size:6.5px;line-height:1.55;color:var(--muted);margin-bottom:10px}
.card .btn-outline{font-size:6px;font-weight:700;border:1px solid var(--navy);color:var(--navy);padding:4px 12px;border-radius:10px;text-decoration:none}
.card.featured{background:var(--red);border-color:var(--red);color:var(--white)}
.card.featured p{color:#ffe3e8}
.card.featured .btn-outline{border-color:var(--white);color:var(--white)}

/* quote band */
.quote-band{position:absolute;top:568px;left:0;width:748px;height:117px;background:linear-gradient(100deg,var(--navy) 0%,var(--navy) 48%,var(--red) 75%,var(--red) 100%)}
.quote-band blockquote{position:absolute;left:190px;top:36px;width:370px;text-align:center;color:var(--white);font-size:12.5px;font-style:italic;font-weight:700;line-height:1.45}
.quote-mark{position:absolute;color:var(--white);font-size:34px;font-weight:700;line-height:1}
.quote-open{left:180px;top:10px}
.quote-close{left:538px;top:72px}

/* about */
.about{position:absolute;top:685px;left:0;width:748px;height:300px;background:var(--white)}
.family-photo{position:absolute;left:144px;top:42px;width:206px;height:220px;background:linear-gradient(160deg,#b8c3c9 0%,#c9a58b 50%,#6f5a4c 100%)}
.about-panel{position:absolute;left:350px;top:62px;width:252px;height:174px;background:var(--navy);color:var(--white);padding:14px 16px}
.about-panel h2{font-size:20px;font-weight:700;margin-bottom:8px}
.about-panel p{font-size:6.5px;line-height:1.6;color:var(--pale);margin-bottom:8px}

/* footer */
.footer{position:absolute;top:985px;left:0;width:748px;height:185px;background:var(--navy)}
.to-top{position:absolute;left:364px;top:-10px}
.footer-contact{position:absolute;left:144px;top:48px;color:var(--white)}
.footer-contact h4{font-size:8px;font-weight:700;letter-spacing:.5px;margin-bottom:10px}
.footer-contact p{font-size:7px;line-height:1.6;color:var(--pale)}
.footer-contact .phone{font-size:11px;font-weight:700;color:var(--white);margin-top:10px}
.footer-brand{position:absolute;left:318px;top:48px;color:var(--white)}
.footer-brand .brand-name{font-size:20px;font-weight:700;line-height:1.2}
.social{display:flex;gap:6px;margin-top:12px}
.social span{width:16px;height:16px;border:1px solid var(--white);border-radius:50%}
.footer-links{position:absolute;left:486px;top:48px;list-style:none}
.footer-links li{font-size:8px;color:var(--white);margin-bottom:10px}
.bottom-bar{position:absolute;top:1170px;left:0;width:748px;height:30px;background:var(--navy-bar);text-align:center;font-size:6px;color:#aab3c8;line-height:30px}
</style>
</head>
<body>

<header class="hero">
  <svg class="hero-shape" width="748" height="350" viewBox="0 0 748 350" aria-hidden="true">
    <path d="M300 0 H748 V350 H470 C420 300 340 250 300 170 C280 120 285 50 300 0 Z" fill="var(--red)"/>
    <path d="M360 0 H748 V350 H560 C480 290 390 220 370 130 C360 80 360 30 360 0 Z" fill="var(--red-soft)" opacity=".35"/>
  </svg>
  <div class="candidate-photo" role="img" aria-label="Portrait of the candidate in judicial robes"></div>
  <nav class="nav">
    <a href="#">HOME</a><a href="#">ABOUT US</a><a href="#">EVENTS</a><a href="#">BLOG</a><a href="#">CONTACT US</a>
    <a href="#" class="nav-cta">DONATE NOW</a>
  </nav>
  <h1 class="hero-title serif">Dana Whitfield for Judge</h1>
  <div class="hero-actions">
    <a href="#" class="btn btn-red">DONATE NOW</a>
    <a href="#" class="btn btn-white">VOLUNTEER</a>
  </div>
</header>

<section class="actions">
  <div class="card">
    <svg class="card-icon" viewBox="0 0 26 26" aria-hidden="true"><circle cx="13" cy="13" r="13" fill="var(--navy)"/><circle cx="10" cy="10" r="3" fill="#fff"/><circle cx="17" cy="10" r="2.5" fill="#fff"/><path d="M5 19c0-4 3-5 5-5s5 1 5 5zM14 19c0-3 2-4 3.5-4s3.5 1 3.5 4z" fill="#fff"/></svg>
    <h3 class="serif">Volunteers</h3>
    <p>Join neighbors who knock doors, make calls and share the message of fair courts across the county.</p>
    <a href="#" class="btn-outline">READ MORE</a>
  </div>
  <div class="card featured">
    <svg class="card-icon" viewBox="0 0 26 26" aria-hidden="true"><circle cx="13" cy="13" r="12" fill="none" stroke="#fff"/><text x="13" y="17.5" text-anchor="middle" font-size="13" font-family="Montserrat,sans-serif" font-weight="700" fill="#fff">$</text></svg>
    <h3 class="serif">Donate</h3>
    <p>Every gift helps us reach voters with mailers, ads and events before the coming election day.</p>
    <a href="#" class="btn-outline">DONATE NOW</a>
  </div>
  <div class="card">
    <svg class="card-icon" viewBox="0 0 26 26" aria-hidden="true"><circle cx="13" cy="13" r="13" fill="var(--navy)"/><rect x="7" y="7" width="12" height="8" fill="#fff"/><rect x="12" y="15" width="2" height="6" fill="#fff"/></svg>
    <h3 class="serif">Get Yard Signs</h3>
    <p>Show your support at home. Request a free yard sign and we will drop it off soon.</p>
    <a href="#" class="btn-outline">READ MORE</a>
  </div>
</section>

<section class="quote-band">
  <span class="quote-mark quote-open serif">&ldquo;</span>
  <blockquote class="serif">For 10 years I've served as an attorney in our area. I've worked to uphold the constitution, be fair, and ensure everyone is given a just trial before our court.</blockquote>
  <span class="quote-mark quote-close serif">&rdquo;</span>
</section>

<section class="about">
  <div class="family-photo" role="img" aria-label="Photo of the candidate with family"></div>
  <div class="about-panel">
    <h2 class="serif">About Us</h2>
    <p>A lifelong resident of this community, I have spent my career in local courtrooms. I believe every person deserves to be heard, treated with respect and judged only by the facts and the law.</p>
    <p>At home I am a spouse and a parent. Our family volunteers at church, coaches youth sports and supports local schools.</p>
    <a href="#" class="btn btn-red">READ MORE</a>
  </div>
</section>

<footer class="footer">
  <svg class="to-top" width="20" height="20" viewBox="0 0 20 20" aria-hidden="true"><circle cx="10" cy="10" r="9" fill="#fff" stroke="var(--navy)"/><path d="M6 8l4 4 4-4" fill="none" stroke="var(--navy)" stroke-width="1.6"/></svg>
  <div class="footer-contact">
    <h4>CONTACT OUR CAMPAIGN</h4>
    <p>P.O. Box 1200<br>Fairview, California, 90000</p>
    <p class="phone">(555) 014-2290</p>
    <p>hello@campaignsite.org</p>
  </div>
  <div class="footer-brand">
    <div class="brand-name serif">Dana Whitfield<br>for Judge</div>
    <div class="social"><span></span><span></span><span></span><span></span></div>
  </div>
  <ul class="footer-links">
    <li>About Us</li><li>Events</li><li>Blog</li><li>Contact Us</li>
  </ul>
</footer>
<div class="bottom-bar">Copyright © 2024 Dana Whitfield for Judge. All Rights Reserved | Privacy Policy</div>

</body>
</html>
```